R Dovak Consulting Design

Our company is a multi-faceted consulting service in specialized areas such as project management and event management.
I would like the design to utilise the colour green, but be simple and unique in concept.
The design should communicate collaboration, openness, trust, efficiency and professionalism.
We like the idea of cogs in a wheel or other geometric designs.

Target Market(s)

Target market is large corporate manufacturers.

Industry/Entity Type

Wheel

Contact Information for Business Card

R Dovak Consulting
Marlene Dovak
Ph. 0438 562 714
Email. marlyfrost@vexorline.on.net
Address. 7 Brambury Ct, Wendale Vic 3299 Australia

```html
<!DOCTYPE html>
<html lang="en">
<head>
<meta charset="utf-8">
<title>R Dovak Consulting – Business Card</title>
<link rel="stylesheet" href="https://fonts.googleapis.com/css2?family=Didact+Gothic&family=Oswald:wght@500&display=swap">
<style>
  :root {
    --backdrop: #e4e6e5;
    --card: #ffffff;
    --band: #1f4a34;
    --accent: #2f8a52;
    --accent-soft: #9fd0b0;
    --ink: #333a36;
    --muted: #4f5752;
    --title: #cfe3d6;
    --on-band: #ffffff;
  }
  * { margin: 0; padding: 0; box-sizing: border-box; }
  html, body { width: 1200px; height: 988px; overflow: hidden; }
  body {
    background: var(--backdrop);
    font-family: "Didact Gothic", Arial, sans-serif;
    color: var(--ink);
    position: relative;
  }

  .card {
    position: absolute;
    left: 239px;
    width: 646px;
    height: 388px;
    background: var(--card);
    box-shadow: 0 4px 14px rgba(0,0,0,.16);
    overflow: hidden;
  }
  .card--front { top: 78px; }
  .card--back { top: 491px; }

  /* Front: ribbon area */
  .ribbon-area {
    position: absolute;
    left: 34px;
    top: 108px;
    width: 576px;
    height: 118px;
    background: linear-gradient(100deg, var(--accent-soft) 0%, var(--accent) 12%, var(--band) 50%, var(--accent) 88%, var(--accent-soft) 100%);
  }
  .banner-url {
    position: absolute;
    left: 186px;
    top: 150px;
    color: var(--on-band);
    font-size: 15px;
    letter-spacing: 2px;
    white-space: nowrap;
    transform: rotate(-3deg);
    transform-origin: left center;
  }

  /* Brand lockup */
  .brand { position: absolute; display: flex; align-items: center; }
  .brand-dot { border-radius: 50%; background: var(--accent); flex: none; }
  .brand-name { color: var(--ink); line-height: 1.12; white-space: nowrap; }
  .brand-name span { display: block; }

  .card--front .brand { left: 186px; top: 240px; }
  .card--front .brand-dot { width: 88px; height: 88px; margin-right: 22px; }
  .card--front .brand-name { font-size: 40px; }
  .card--front .brand-name span + span { font-size: 32px; }

  .card--back .brand { left: 28px; top: 122px; }
  .card--back .brand-dot { width: 86px; height: 86px; margin-right: 16px; }
  .card--back .brand-name { font-size: 38px; }
  .card--back .brand-name span + span { font-size: 30px; }

  /* Back: band and fold area */
  .name-band {
    position: absolute;
    left: 0; top: 0;
    width: 492px;
    height: 98px;
    background: var(--band);
  }
  .fold-area {
    position: absolute;
    left: 492px;
    top: 0;
    width: 132px;
    height: 340px;
    background: linear-gradient(160deg, var(--accent-soft) 0%, var(--accent) 30%, var(--band) 75%);
  }
  .holder { position: absolute; left: 22px; top: 14px; color: var(--on-band); }
  .holder-name {
    font-family: "Oswald", "Arial Narrow", sans-serif;
    font-weight: 500;
    font-size: 40px;
    line-height: 1.05;
    letter-spacing: 0.5px;
    white-space: nowrap;
  }
  .holder-title {
    font-size: 15px;
    letter-spacing: 1.6px;
    color: var(--title);
    margin-top: 6px;
  }

  .contact-list {
    position: absolute;
    left: 22px;
    top: 240px;
    list-style: none;
    font-size: 10px;
    color: var(--muted);
  }
  .contact-list li { display: flex; align-items: center; height: 23px; white-space: nowrap; }
  .contact-list svg { width: 12px; height: 12px; margin-right: 7px; flex: none; color: var(--accent); }
</style>
</head>
<body>

<section class="card card--front" aria-label="Business card front">
  <div class="ribbon-area" role="img" aria-label="Folded ribbon banner illustration"></div>
  <div class="banner-url">www.dovakconsult.net</div>
  <div class="brand">
    <div class="brand-dot"></div>
    <div class="brand-name"><span>R Dovak</span><span>Consulting</span></div>
  </div>
</section>

<section class="card card--back" aria-label="Business card back">
  <div class="name-band"></div>
  <div class="fold-area" role="img" aria-label="Folded ribbon illustration"></div>

  <div class="holder">
    <div class="holder-name">MARLENE DOVAK</div>
    <div class="holder-title">GENERAL MANAGER</div>
  </div>

  <div class="brand">
    <div class="brand-dot"></div>
    <div class="brand-name"><span>R Dovak</span><span>Consulting</span></div>
  </div>

  <ul class="contact-list">
    <li><svg viewBox="0 0 12 12" aria-hidden="true"><circle cx="6" cy="6" r="5.4" fill="none" stroke="currentColor" stroke-width=".8"/><path d="M4 3.3l1 1.2-.5.7a4 4 0 0 0 2.3 2.3l.7-.5 1.2 1-.6.9C6.3 8.8 3.2 5.7 3.1 3.9z" fill="currentColor"/></svg>0438 562 714</li>
    <li><svg viewBox="0 0 12 12" aria-hidden="true"><circle cx="6" cy="6" r="5.4" fill="none" stroke="currentColor" stroke-width=".8"/><rect x="4.3" y="2.8" width="3.4" height="6.4" rx=".6" fill="none" stroke="currentColor" stroke-width=".8"/></svg>03 9554 2180</li>
    <li><svg viewBox="0 0 12 12" aria-hidden="true"><circle cx="6" cy="6" r="5.4" fill="none" stroke="currentColor" stroke-width=".8"/><rect x="3.3" y="4.5" width="5.4" height="3.5" fill="none" stroke="currentColor" stroke-width=".8"/><rect x="4.3" y="3" width="3.4" height="1.5" fill="currentColor"/></svg>03 9554 2181</li>
    <li><svg viewBox="0 0 12 12" aria-hidden="true"><circle cx="6" cy="6" r="5.4" fill="none" stroke="currentColor" stroke-width=".8"/><rect x="3.2" y="4" width="5.6" height="4" fill="none" stroke="currentColor" stroke-width=".8"/><path d="M3.2 4L6 6.2 8.8 4" fill="none" stroke="currentColor" stroke-width=".8"/></svg>marlyfrost@vexorline.on.net</li>
    <li><svg viewBox="0 0 12 12" aria-hidden="true"><circle cx="6" cy="6" r="5.4" fill="none" stroke="currentColor" stroke-width=".8"/><circle cx="6" cy="6" r="2.9" fill="none" stroke="currentColor" stroke-width=".7"/><path d="M3.1 6h5.8M6 3.1v5.8" stroke="currentColor" stroke-width=".6"/></svg>www.dovakconsult.net</li>
    <li><svg viewBox="0 0 12 12" aria-hidden="true"><circle cx="6" cy="6" r="5.4" fill="none" stroke="currentColor" stroke-width=".8"/><path d="M6 9.2L4 6a2.2 2.2 0 1 1 4 0z" fill="currentColor"/><circle cx="6" cy="5" r=".8" fill="#fff"/></svg>7 Brambury Ct, Wendale Vic 3299 Australia</li>
  </ul>
</section>

</body>
</html>
```